Brochure / Leaflet Required

Hi!
We need a cool brochure / leaflet for our Plexon product line.
These are plastic corrugated sheets which are used to make various products.
When you look at the Plexon section on our website: http://velmarto.example/plexon/ you will get a bit more info (the website is under construction).
We need a separate page for a few products.
But for now we need just one test page for the first product group "Surface Protection". If your design is approved as a template, we will give you the text and pics for the other products. We can set a price per page for the other pages later.
Requirements:
- Size should be A4. The leaflet will be combined into one full brochure at the end. But each page will also need to function a a separate leaflet for that particular product. (For example it will also be placed on the website as a downloadable PDF)
- Font needs to be Gill Sans MT
- This is the brand logo: https://files.quorvik.example/s/k2b81tdex9ma3q1/Plexon%20logo%20-%20registered.ai?dl=0
- These 3 pics should be use on leaflet: https://files.quorvik.example/sh/71xq4mbn2vk8r0w/BBDm8upSwgoMvYZ3LLx5rRhWb?dl=0
- Here you can find the text: https://files.quorvik.example/s/p9h27wlcrzt45ej/Text%20-%20Surface%20Protection.docx?dl=0
- The icons in this text part (including text) also need to be placed in the brochure. The originals can be found here: https://files.quorvik.example/sh/83jm51640hgo2tz/BBEqtZZZ3xxt3NbAxaznv6nLb?dl=0
Please think outside of the box as much as possible.
And make sure to use mainly white and the "Plexon logo" blue.
We also have another product group which will need to be done after this project.
Looking forward to your design!
Regards,
Teun
Target Market(s)
Construction
Industry/Entity Type
Plastic
Look and feel

```html
<!DOCTYPE html>
<html lang="en">
<head>
<meta charset="utf-8">
<title>Plexon – Surface Protection leaflet</title>
<link rel="stylesheet" href="https://fonts.googleapis.com/css2?family=Cabin:wght@400;600&display=swap">
<style>
  :root {
    --brand-blue: #2f6fb3;
    --page: #eceded;
    --rail: #c4c6c9;
    --band: #d7d8db;
    --panel: #e6e7e9;
    --ink: #5f6165;
    --rule: #8f9297;
    --backdrop: #f4f4f4;
  }
  * { box-sizing: border-box; margin: 0; padding: 0; }
  html, body { width: 1200px; height: 803px; overflow: hidden; background: var(--backdrop); }
  body { font-family: "Cabin", "Gill Sans", sans-serif; color: var(--ink); }

  .leaflet {
    position: absolute; inset: 0;
    width: 1200px; height: 803px; overflow: hidden;
    background: var(--page);
    display: grid;
    grid-template-columns: 150px 1fr;
  }
  .leaflet__rail { background: var(--rail); }
  .leaflet__body { padding: 24px 70px 0 0; display: flex; flex-direction: column; }

  .feature-list { list-style: none; display: flex; flex-direction: column; gap: 12px; }
  .feature { position: relative; }
  .feature__icon {
    position: absolute; left: -118px; top: 22px;
    width: 48px; height: 48px;
  }
  .feature__title {
    background: var(--band);
    color: var(--brand-blue);
    font-weight: 600; font-size: 22px; line-height: 1.2; letter-spacing: .2px;
    padding: 6px 0 6px 26px;
  }
  .feature__text {
    background: var(--panel);
    font-size: 16px; line-height: 1.3;
    padding: 8px 26px 11px;
  }

  .signoff {
    margin-top: 34px; position: relative; height: 110px;
  }
  .signoff__rule {
    position: absolute; left: 120px; right: 60px; top: 14px;
    height: 2px; background: var(--rule);
  }
  .signoff__dot {
    position: absolute; left: 50%; top: 9px; width: 12px; height: 12px;
    margin-left: -6px; border-radius: 50%; background: var(--rule);
  }
  .signoff__brand {
    position: absolute; left: 0; right: 0; top: 34px; text-align: center;
    font-size: 48px; line-height: 1.1; font-weight: 600; color: var(--brand-blue); letter-spacing: .5px;
  }
</style>
</head>
<body>
<main class="leaflet">
  <aside class="leaflet__rail"></aside>
  <section class="leaflet__body">
    <ul class="feature-list">
      <li class="feature">
        <svg class="feature__icon" viewBox="0 0 50 50" aria-hidden="true"><circle cx="25" cy="25" r="24" fill="#fff"/><circle cx="25" cy="25" r="20" fill="var(--brand-blue)"/><rect x="15" y="22" width="20" height="12" rx="2" fill="#fff"/><path d="M20 22 L22 16 H28 L30 22" stroke="#fff" stroke-width="2" fill="none"/></svg>
        <h2 class="feature__title">Weight</h2>
        <p class="feature__text">The weight of Plexon sheets ranges from 250 to 1500 GSM, the strongest option for heavy surface protection.</p>
      </li>
      <li class="feature">
        <svg class="feature__icon" viewBox="0 0 50 50" aria-hidden="true"><circle cx="25" cy="25" r="24" fill="#fff"/><circle cx="25" cy="25" r="20" fill="var(--brand-blue)"/><path d="M14 31 H36 M14 31 V19 M36 31 V19 M18 25 H32" stroke="#fff" stroke-width="2.5" fill="none"/></svg>
        <h2 class="feature__title">Size</h2>
        <p class="feature__text">Plexon sheets are available in any required size. The length is limited to 240 cm.</p>
      </li>
      <li class="feature">
        <svg class="feature__icon" viewBox="0 0 50 50" aria-hidden="true"><circle cx="25" cy="25" r="24" fill="#fff"/><circle cx="25" cy="25" r="20" fill="var(--brand-blue)"/><path d="M25 13 C31 21 33 25 33 29 A8 8 0 0 1 17 29 C17 25 19 21 25 13 Z" fill="#fff"/></svg>
        <h2 class="feature__title">Color</h2>
        <p class="feature__text">Our customers can choose any color for the sheets or artwork. We are glad to provide you with a sample.</p>
      </li>
      <li class="feature">
        <svg class="feature__icon" viewBox="0 0 50 50" aria-hidden="true"><circle cx="25" cy="25" r="24" fill="#fff"/><circle cx="25" cy="25" r="20" fill="var(--brand-blue)"/><path d="M21 13 H29 M23 13 V22 L15 35 H35 L27 22 V13" stroke="#fff" stroke-width="2.2" fill="none" stroke-linejoin="round"/><path d="M19 30 H31 L33 34 H17 Z" fill="#fff"/></svg>
        <h2 class="feature__title">Virgin and Recycled Polypropylene</h2>
        <p class="feature__text">We can use 100% virgin polypropylene to produce your sheets. Another option is to let us recycle up to 20% of our internally regenerated polypropylene.</p>
      </li>
      <li class="feature">
        <svg class="feature__icon" viewBox="0 0 50 50" aria-hidden="true"><circle cx="25" cy="25" r="24" fill="#fff"/><circle cx="25" cy="25" r="20" fill="var(--brand-blue)"/><circle cx="20" cy="21" r="5" fill="none" stroke="#fff" stroke-width="2"/><circle cx="30" cy="21" r="5" fill="none" stroke="#fff" stroke-width="2"/><circle cx="25" cy="30" r="5" fill="none" stroke="#fff" stroke-width="2"/></svg>
        <h2 class="feature__title">Custom Printing</h2>
        <p class="feature__text">Plexon sheets can be supplied with high-resolution, full-color printing. Send us your design and we can directly print it onto the sheets in our factory.</p>
      </li>
      <li class="feature">
        <svg class="feature__icon" viewBox="0 0 50 50" aria-hidden="true"><circle cx="25" cy="25" r="24" fill="#fff"/><circle cx="25" cy="25" r="20" fill="var(--brand-blue)"/><path d="M25 12 C28 18 34 21 34 29 A9 9 0 0 1 16 29 C16 24 19 22 21 18 C22 22 24 23 25 24 C26 20 26 16 25 12 Z" fill="#fff"/><path d="M25 26 C27 29 29 30 29 33 A4 4 0 0 1 21 33 C21 30 23 29 25 26 Z" fill="var(--brand-blue)"/></svg>
        <h2 class="feature__title">Fire-Retardant Sheets</h2>
        <p class="feature__text">A fire-retardant version of Plexon sheets is available. Please let us know the fire rating you require, and we are happy to produce them for you.</p>
      </li>
    </ul>
    <footer class="signoff">
      <div class="signoff__rule"></div>
      <div class="signoff__dot"></div>
      <p class="signoff__brand">Plexon</p>
    </footer>
  </section>
</main>
</body>
</html>
```